Business Card design for Recruiter providing Recruitment Staff Augmentation services

I need a double sided business card. I have used Zek to print cards in the past and really like their quality. I have a logo but need to change the tagline that is part of the graphic.

The tagline currently reads and Connnecting people with careers - but it should be removed.

The back should look like a notecard for writing a to do list with the first to-do Augment Recruiting Staff

```html
<!DOCTYPE html>
<html lang="en">
<head>
<meta charset="utf-8">
<title>Talent Summit – Business Card</title>
<link rel="stylesheet" href="https://fonts.googleapis.com/css2?family=Montserrat:wght@400;600;700&family=Open+Sans:wght@400;600&display=swap">
<style>
  :root {
    --backdrop: #2b2b2d;
    --card-blue: #174a66;
    --card-blue-dark: #0f3a52;
    --card-white: #f7f7f7;
    --navy: #1d3e57;
    --accent-red: #b73a22;
    --text-grey: #2e2e2e;
    --white: #ffffff;
    --rule-light: rgba(255,255,255,.35);
  }
  * { box-sizing: border-box; margin: 0; padding: 0; }
  html, body {
    width: 1200px; height: 997px; overflow: hidden;
    background: var(--backdrop);
  }
  .canvas { position: relative; width: 1200px; height: 997px; }
  .card {
    position: absolute; width: 500px; height: 286px;
    border-radius: 18px; overflow: hidden;
    box-shadow: 0 18px 40px rgba(0,0,0,.45);
  }

  /* Back side: notecard for a to-do list */
  .card--back {
    left: 70px; top: 355px;
    background: radial-gradient(ellipse at 45% 40%, var(--card-blue) 0%, var(--card-blue-dark) 100%);
    padding: 30px 36px;
    font-family: "Montserrat", sans-serif;
    color: var(--white);
  }
  .back-brand {
    display: flex; align-items: center; gap: 12px;
    padding-bottom: 12px; border-bottom: 1.5px solid var(--white);
  }
  .back-brand__mark {
    width: 26px; height: 26px; border-radius: 50%;
    border: 3px solid var(--white);
  }
  .back-brand__name {
    font-weight: 400; font-size: 24px; letter-spacing: 2px; line-height: 1;
  }
  .todo { list-style: none; margin-top: 8px; }
  .todo li {
    display: flex; align-items: flex-end; gap: 12px;
    height: 40px; padding-bottom: 7px;
    border-bottom: 1px solid var(--rule-light);
  }
  .todo__box {
    flex: none; width: 16px; height: 16px;
    border: 2px solid var(--white); border-radius: 2px;
  }
  .todo__text {
    font-family: "Open Sans", sans-serif; font-weight: 600;
    font-size: 15px; line-height: 1;
  }

  /* Front side */
  .card--front {
    left: 630px; top: 355px;
    background: linear-gradient(160deg, var(--white) 0%, var(--card-white) 60%, #e9e9e9 100%);
    font-family: "Open Sans", sans-serif;
  }
  .front-brand {
    position: absolute; left: 34px; top: 36px;
    display: flex; align-items: center; gap: 10px;
  }
  .front-brand__dot {
    width: 26px; height: 26px; border-radius: 50%; background: var(--accent-red);
  }
  .front-brand__name {
    font-family: "Montserrat", sans-serif; font-weight: 400;
    font-size: 26px; letter-spacing: 1.5px; color: var(--navy);
  }
  .rule { position: absolute; height: 1.5px; background: var(--navy); }
  .rule--brand { left: 34px; right: 30px; top: 80px; }
  .rule--name { left: 196px; right: 30px; top: 132px; }
  .holder { position: absolute; left: 34px; top: 114px; }
  .holder__name {
    font-family: "Montserrat", sans-serif; font-weight: 700;
    font-size: 19px; color: var(--navy); line-height: 1.1;
  }
  .holder__role {
    font-family: "Montserrat", sans-serif; font-weight: 600;
    font-size: 11px; letter-spacing: .6px; color: var(--accent-red);
  }
  .contacts { position: absolute; left: 34px; top: 172px; list-style: none; }
  .contacts li {
    display: flex; align-items: flex-start; gap: 10px;
    font-size: 12.5px; color: var(--text-grey); line-height: 1.3; margin-bottom: 9px;
  }
  .contacts svg { flex: none; width: 15px; height: 15px; margin-top: 1px; }
  .website {
    position: absolute; right: 30px; top: 172px;
    font-family: "Montserrat", sans-serif; font-weight: 600;
    font-size: 13px; color: var(--accent-red);
  }
</style>
</head>
<body>
<main class="canvas">
  <section class="card card--back" aria-label="Card back, to-do notecard">
    <div class="back-brand">
      <span class="back-brand__mark"></span>
      <span class="back-brand__name">TALENT SUMMIT</span>
    </div>
    <ul class="todo">
      <li><span class="todo__box"></span><span class="todo__text">Augment Recruiting Staff</span></li>
      <li><span class="todo__box"></span></li>
      <li><span class="todo__box"></span></li>
      <li><span class="todo__box"></span></li>
      <li><span class="todo__box"></span></li>
    </ul>
  </section>

  <section class="card card--front" aria-label="Card front">
    <div class="front-brand">
      <span class="front-brand__dot"></span>
      <span class="front-brand__name">TALENT SUMMIT</span>
    </div>
    <div class="rule rule--brand"></div>

    <div class="holder">
      <p class="holder__name">Dana Whitfield</p>
      <p class="holder__role">FOUNDER &amp; CEO</p>
    </div>
    <div class="rule rule--name"></div>

    <ul class="contacts">
      <li>
        <svg viewBox="0 0 16 16" aria-hidden="true"><circle cx="8" cy="8" r="8" fill="#b73a22"/><path d="M5 4.5c.5-.4 1-.3 1.3.2l.6 1.1c.2.4.1.8-.2 1l-.4.3c.4.9 1.1 1.6 2 2l.3-.4c.2-.3.6-.4 1-.2l1.1.6c.5.3.6.8.2 1.3-.6.7-1.5.9-2.4.5C6.6 10 5.9 9.3 5 7.6c-.4-.9-.3-2.3 0-3.1z" fill="#fff"/></svg>
        <span>+1 (203) 555-0142</span>
      </li>
      <li>
        <svg viewBox="0 0 16 16" aria-hidden="true"><circle cx="8" cy="8" r="8" fill="#b73a22"/><path d="M8 4l4 3.4h-1.2V11.5H9V9H7v2.5H5.2V7.4H4z" fill="#fff"/></svg>
        <span>Unit 42, Block 7, Pune</span>
      </li>
      <li>
        <svg viewBox="0 0 16 16" aria-hidden="true"><circle cx="8" cy="8" r="8" fill="#b73a22"/><path d="M8 3.5a2.8 2.8 0 0 0-2.8 2.8C5.2 8.5 8 12.5 8 12.5s2.8-4 2.8-6.2A2.8 2.8 0 0 0 8 3.5zm0 3.9a1.1 1.1 0 1 1 0-2.2 1.1 1.1 0 0 1 0 2.2z" fill="#fff"/></svg>
        <span>18 Maple Ridge Road, 2nd Floor,<br>Stamford, CT 06901</span>
      </li>
    </ul>

    <p class="website">www.talentsummit.com</p>
  </section>
</main>
</body>
</html>
```